Business Card Design for Cybersecurity Company - QuorvaNet Systems

We need a business card design for our new cybersecurity company, QuorvaNet. We’re going for a clean, hi tech look that feels modern, premium, and trustworthy. We want a design that really stands out and makes people say WOW when we hand it over!

QuorvaNet delivers reliable IT support and managed services for small and mid sized businesses. We help companies stay secure, efficient, and connected through proactive monitoring, cybersecurity services, cloud management, and remote support.

Target Market(s)

Designers should target small and mid sized businesses that need dependable cybersecurity and IT support.

Industry/Entity Type

Cybersecurity, Managed Service Provider, IT services

Contact Information for Business Card

Contact information

Requirements
Must have
• The card should look clean, modern, and tech focused, with the QuorvaNet logo, clear contact info, and strong readability. It needs to feel premium and professional while still keeping a simple layout that fits a cybersecurity and IT brand.
Nice to have
• Nice to have elements include subtle touches that give the card a modern, tech feel, along with a layout that works well in different background styles.
Should not have
• The card should avoid clutter, loud graphics, or anything that takes attention away from the logo and contact details.

```html
<!DOCTYPE html>
<html lang="en">
<head>
<meta charset="utf-8">
<title>QuorvaNet Systems – Business Card</title>
<link rel="stylesheet" href="https://fonts.googleapis.com/css2?family=Open+Sans:wght@400;600;700&display=swap">
<style>
  :root {
    --backdrop-top: #e4e3e0;
    --backdrop-bottom: #bdbcb8;
    --card: #222222;
    --ink-light: #f1f1f3;
    --ink-muted: #c9c9cf;
    --blue: #2f80f7;
    --indigo: #4e55f3;
    --violet: #7a2cf0;
  }
  * { box-sizing: border-box; margin: 0; padding: 0; }
  html, body { width: 1200px; height: 801px; overflow: hidden; }
  body {
    background: linear-gradient(160deg, var(--backdrop-top), var(--backdrop-bottom));
    font-family: "Open Sans", Arial, sans-serif;
    display: flex;
    align-items: center;
    justify-content: center;
    gap: 40px;
  }
  .card {
    position: relative;
    width: 540px;
    height: 309px;
    background: var(--card);
    border-radius: 2px;
    box-shadow: 0 14px 30px rgba(0,0,0,.28);
    overflow: hidden;
  }
  .card::after {
    content: "";
    position: absolute;
    left: 0; right: 0; bottom: 0;
    height: 3px;
    background: linear-gradient(90deg, var(--blue), var(--violet));
  }

  /* contact side */
  .contact-card { display: flex; align-items: center; padding: 0 34px; }
  .contact-brand {
    width: 170px;
    display: flex;
    align-items: center;
    gap: 10px;
  }
  .brand-dot {
    width: 18px; height: 18px;
    border-radius: 50%;
    background: var(--indigo);
    flex: none;
  }
  .brand-name {
    font-weight: 600;
    color: var(--indigo);
    font-size: 21px;
    letter-spacing: .2px;
  }
  .divider {
    width: 1px;
    height: 150px;
    margin: 0 26px 0 10px;
    background: linear-gradient(180deg, var(--blue), var(--violet));
  }
  .person-name {
    font-weight: 700;
    font-size: 21px;
    letter-spacing: .5px;
    text-transform: uppercase;
    background: linear-gradient(90deg, var(--blue), var(--violet));
    -webkit-background-clip: text;
    background-clip: text;
    color: transparent;
  }
  .person-role {
    color: var(--ink-light);
    font-size: 12.5px;
    margin: 2px 0 18px;
  }
  .contact-list { list-style: none; }
  .contact-list li {
    display: flex;
    align-items: center;
    gap: 9px;
    color: var(--ink-light);
    font-size: 13px;
    line-height: 21px;
  }
  .contact-list svg { width: 12px; height: 12px; flex: none; }

  /* logo side */
  .logo-card { display: flex; align-items: center; justify-content: center; gap: 14px; }
  .logo-card .brand-dot { width: 30px; height: 30px; }
  .logo-card .brand-name { font-size: 40px; }
</style>
</head>
<body>

  <section class="card contact-card" aria-label="Contact side">
    <div class="contact-brand">
      <span class="brand-dot"></span>
      <span class="brand-name">QuorvaNet</span>
    </div>
    <div class="divider"></div>
    <div class="contact-details">
      <h1 class="person-name">Dana Merrick</h1>
      <p class="person-role">Owner | CEO | QuorvaNet Systems</p>
      <ul class="contact-list">
        <li>
          <svg viewBox="0 0 12 12" aria-hidden="true"><path d="M2.5 1 4.3 3 3.4 4.3c.6 1.5 1.8 2.7 3.3 3.3L8 6.7 10 8.5 9 10.5C5 10.3 1.7 7 1.5 3Z" fill="var(--indigo)"/></svg>
          (855) 214-7830
        </li>
        <li>
          <svg viewBox="0 0 12 12" aria-hidden="true"><rect x="3" y=".8" width="6" height="10.4" rx="1" fill="none" stroke="var(--indigo)" stroke-width="1.2"/></svg>
          (813) 310-2287
        </li>
        <li>
          <svg viewBox="0 0 12 12" aria-hidden="true"><rect x=".8" y="2.2" width="10.4" height="7.6" rx=".8" fill="none" stroke="var(--violet)" stroke-width="1.2"/><path d="M1 2.6 6 6.6 11 2.6" fill="none" stroke="var(--violet)" stroke-width="1.2"/></svg>
          dana@quorvanet.com
        </li>
        <li>
          <svg viewBox="0 0 12 12" aria-hidden="true"><circle cx="6" cy="6" r="5" fill="none" stroke="var(--violet)" stroke-width="1.1"/><ellipse cx="6" cy="6" rx="2.2" ry="5" fill="none" stroke="var(--violet)" stroke-width="1"/><path d="M1 6h10" stroke="var(--violet)" stroke-width="1"/></svg>
          quorvanet.com
        </li>
      </ul>
    </div>
  </section>

  <section class="card logo-card" aria-label="Brand side">
    <span class="brand-dot"></span>
    <span class="brand-name">QuorvaNet Systems</span>
  </section>

</body>
</html>
```